New Business Card Design Project

I have a logo I would like to use on the business card. I want something that will stand out and that will be remembered.

Target Market(s)

People who collect gems, minerals and crystals.

Contact Information for Business Card

email - tkstonefalcon@mailbrook.net
phone # 617-203-4958

Font styles to use
Serif
Sans Serif
Decorative

Colors

Designer to choose colors to be used in the design.

Requirements
Must have
• The logo...two to choose from.
Nice to have
• An eye catching and memorable way to draw in people who collect gems minerals and crystals.

```html
<!DOCTYPE html>
<html lang="en">
<head>
<meta charset="utf-8">
<title>Stone Falcon – Business Card</title>
<link href="https://fonts.googleapis.com/css2?family=Lato:wght@400;700;900&display=swap" rel="stylesheet">
<style>
  :root {
    --backdrop: #6a6a6a;
    --card-light: #ffffff;
    --card-dark: #000000;
    --ink: #111111;
    --accent: #1a10d6;
    --white: #ffffff;
  }
  * { margin: 0; padding: 0; box-sizing: border-box; }
  html, body { width: 1200px; height: 900px; overflow: hidden; }
  body {
    background: var(--backdrop);
    position: relative;
    font-family: "Lato", Arial, sans-serif;
  }
  .card {
    position: absolute;
    top: 200px;
    width: 310px;
    height: 502px;
    box-shadow: 3px 4px 8px rgba(0,0,0,0.35);
  }
  .card--front {
    left: 253px;
    background: var(--card-light);
    border-radius: 50px 0 50px 0;
  }
  .card--back {
    left: 627px;
    background: var(--card-dark);
    border-radius: 0 50px 0 50px;
  }
  .brand {
    position: absolute;
    left: 0; right: 0;
    display: flex;
    flex-direction: column;
    align-items: center;
    gap: 22px;
  }
  .card--front .brand { top: 62px; }
  .card--back .brand { top: 150px; }
  .brand__mark {
    width: 96px; height: 96px;
    border-radius: 50%;
  }
  .card--front .brand__mark { background: var(--ink); }
  .card--back .brand__mark { background: var(--white); }
  .brand__name {
    font-weight: 900;
    font-size: 36px;
    letter-spacing: 0.5px;
    line-height: 1;
  }
  .card--front .brand__name { color: var(--ink); }
  .card--back .brand__name { color: var(--white); }

  .contact {
    position: absolute;
    left: 33px;
    top: 322px;
    color: var(--ink);
  }
  .contact__name {
    color: var(--accent);
    font-weight: 700;
    font-size: 20px;
    line-height: 24px;
  }
  .contact__role {
    font-size: 14px;
    line-height: 18px;
    margin-bottom: 8px;
  }
  .contact__list { list-style: none; }
  .contact__item {
    display: flex;
    align-items: center;
    gap: 4px;
    font-size: 14px;
    line-height: 18px;
  }
  .contact__icon { width: 13px; height: 13px; flex: none; }
  .contact__address {
    margin-top: 6px;
    font-size: 14px;
    line-height: 18px;
    font-style: normal;
  }
  .web {
    position: absolute;
    left: 0; right: 0;
    top: 442px;
    text-align: center;
    color: var(--accent);
    font-weight: 700;
    font-size: 13px;
  }
</style>
</head>
<body>
  <section class="card card--front">
    <div class="brand">
      <span class="brand__mark"></span>
      <span class="brand__name">STONE FALCON</span>
    </div>
    <div class="contact">
      <p class="contact__name">TARA KELL</p>
      <p class="contact__role">Managing Director</p>
      <ul class="contact__list">
        <li class="contact__item">
          <svg class="contact__icon" viewBox="0 0 16 16"><path fill="#1a10d6" d="M2 5c0-2 3-3 6-3s6 1 6 3v1h-3V5H5v1H2z M4 7h8l2 6H2z"/><circle cx="8" cy="10" r="1.6" fill="#fff"/></svg>
          617-203-4958
        </li>
        <li class="contact__item">
          <svg class="contact__icon" viewBox="0 0 16 16"><rect x="1" y="3" width="14" height="10" fill="#1a10d6"/><path d="M1.5 3.5 8 9l6.5-5.5" stroke="#fff" stroke-width="1.3" fill="none"/></svg>
          tkstonefalcon@mailbrook.net
        </li>
        <li class="contact__item">
          <svg class="contact__icon" viewBox="0 0 16 16"><circle cx="8" cy="8" r="7" fill="#1a10d6"/><path d="M5 4c2 1 1 3 3 3s1 3 3 4M9 3c1 1 3 1 3 3" stroke="#fff" stroke-width="1.2" fill="none"/></svg>
          www.stonefalconmin.com
        </li>
      </ul>
      <address class="contact__address">421, Address line here,<br>45452,Country Name</address>
    </div>
  </section>

  <section class="card card--back">
    <div class="brand">
      <span class="brand__mark"></span>
      <span class="brand__name">STONE FALCON</span>
    </div>
    <p class="web">www.stonefalconmin.com</p>
  </section>
</body>
</html>
```